Graphic Design of Business Process

We require an eye-catching, sophisticated design of 2 business processes (attached), that will be used digitally AND for print (to be put on walls in our office).

The basic layout is attached. We require a creative, professional designer to re-design these so that they look appealing but still able to grasp all the information.

We will require vector files and editable project files for final delivery. You may refer to our website (kitefieldmedia.com.au) for an indication of our brand.

If you have any questions, please ask.

Thank you.

```html
<!DOCTYPE html>
<html lang="en">
<head>
<meta charset="utf-8">
<title>Sales Content Funnel &amp; Content Hierarchy</title>
<link rel="stylesheet" href="https://fonts.googleapis.com/css2?family=Montserrat:wght@300;400;600;700;800;900&display=swap">
<style>
  :root {
    --navy-deep: #0a3f73;
    --navy: #0d5596;
    --blue: #1577c0;
    --blue-light: #3fa3e3;
    --sky: #8fd0f7;
    --sky-pale: #c9ebfd;
    --tab-face: #5bb6ee;
    --tab-side: #2a86c9;
    --orange: #f7811f;
    --orange-dark: #d9640d;
    --amber: #fbb224;
    --amber-dark: #e08f10;
    --yellow: #fde43a;
    --red: #ef5a1e;
    --red-dark: #b8300f;
    --ink: #0c3765;
    --white: #ffffff;
  }
  html, body { margin: 0; padding: 0; overflow: hidden; }
  body { width: 793px; height: 1200px; font-family: "Montserrat", sans-serif; }
  .canvas { display: block; width: 793px; height: 1200px; }
  .title-bold { font-weight: 900; }
  .title-light { font-weight: 300; }
  .tab-head { font-weight: 800; font-size: 15px; fill: var(--white); }
  .tab-sub { font-weight: 700; font-size: 9px; fill: var(--ink); }
  .tab-note { font-weight: 400; font-size: 7px; fill: var(--white); }
  .band-head { font-weight: 800; fill: var(--white); }
  .band-note { font-weight: 600; font-size: 8px; fill: var(--white); }
  .wom { font-weight: 800; font-size: 22px; fill: var(--sky-pale); }
  .tier-head { font-weight: 900; font-size: 28px; }
  .tier-sub { font-weight: 800; }
</style>
</head>
<body>
<svg class="canvas" viewBox="0 0 793 1200" xmlns="http://www.w3.org/2000/svg">
  <defs>
    <radialGradient id="bg-top" cx="50%" cy="40%" r="70%">
      <stop offset="0" stop-color="#1b7fca"/>
      <stop offset="1" stop-color="#0a4a86"/>
    </radialGradient>
    <radialGradient id="bg-bottom" cx="50%" cy="60%" r="70%">
      <stop offset="0" stop-color="#1b7fca"/>
      <stop offset="1" stop-color="#0a4a86"/>
    </radialGradient>
    <linearGradient id="orange-band" x1="0" x2="1">
      <stop offset="0" stop-color="#ffa045"/><stop offset="0.6" stop-color="#f7811f"/><stop offset="1" stop-color="#d9640d"/>
    </linearGradient>
    <linearGradient id="amber-band" x1="0" x2="1">
      <stop offset="0" stop-color="#ffc64a"/><stop offset="0.6" stop-color="#fbb224"/><stop offset="1" stop-color="#e08f10"/>
    </linearGradient>
    <linearGradient id="yellow-band" x1="0" x2="1">
      <stop offset="0" stop-color="#fff06a"/><stop offset="0.6" stop-color="#fde43a"/><stop offset="1" stop-color="#e6c21b"/>
    </linearGradient>
    <clipPath id="pyramid-front"><polygon points="396,765 206,1135 520,1135"/></clipPath>
    <marker id="arrow-head" markerWidth="8" markerHeight="8" refX="4" refY="4" orient="auto">
      <path d="M0,0 L8,4 L0,8 Z" fill="var(--sky-pale)"/>
    </marker>
  </defs>

  <!-- Backgrounds -->
  <rect x="0" y="0" width="793" height="598" fill="url(#bg-top)"/>
  <rect x="0" y="598" width="793" height="602" fill="url(#bg-bottom)"/>
  <rect class="section-divider" x="0" y="594" width="793" height="6" fill="var(--navy-deep)" opacity="0.6"/>

  <!-- Funnel title -->
  <g class="funnel-title">
    <text class="title-bold" x="248" y="72" font-size="56" fill="var(--sky)">SALES</text>
    <text class="title-light" x="460" y="42" font-size="26" fill="var(--sky)">CONTENT</text>
    <text class="title-light" x="460" y="72" font-size="26" fill="var(--sky)">FUNNEL</text>
  </g>

  <!-- Stage tabs -->
  <g class="stage-tabs">
    <g class="tab">
      <polygon points="66,178 300,178 322,208 300,238 66,238" fill="var(--tab-face)"/>
      <polygon points="300,178 322,208 300,238 312,208" fill="var(--tab-side)"/>
      <text class="tab-head" x="88" y="198">AWARENESS</text>
      <text class="tab-sub" x="88" y="212">IDENTIFY PROBLEM/NEED</text>
      <text class="tab-note" x="110" y="228">SHOW THE OUTCOME, NOT THE PRODUCT</text>
    </g>
    <g class="tab">
      <polygon points="66,290 300,290 322,322 300,355 66,355" fill="var(--tab-face)"/>
      <polygon points="300,290 322,322 300,355 312,322" fill="var(--tab-side)"/>
      <text class="tab-head" x="88" y="310">CONSIDERATION</text>
      <text class="tab-sub" x="88" y="324">EVALUATE ALTERNATIVES</text>
      <text class="tab-note" x="88" y="336">WHY THIS SOLUTION BEATS OTHERS</text>
      <text class="tab-note" x="88" y="346">HOW THIS PROVIDER MEETS MY NEED</text>
    </g>
    <g class="tab">
      <polygon points="66,395 300,395 322,427 300,460 66,460" fill="var(--tab-face)"/>
      <polygon points="300,395 322,427 300,460 312,427" fill="var(--tab-side)"/>
      <text class="tab-head" x="88" y="416">ACTION/DECISION</text>
      <text class="tab-sub" x="88" y="430">PRESENT AN OFFER</text>
      <text class="tab-note" x="196" y="448">REMOVE ANY BARRIERS</text>
    </g>
  </g>

  <!-- Funnel -->
  <g class="funnel">
    <path d="M250,145 A172,18 0 0 0 594,145 L554,278 A132,14 0 0 1 290,278 Z" fill="url(#orange-band)"/>
    <ellipse cx="422" cy="145" rx="172" ry="18" fill="#ffb066"/>
    <ellipse cx="422" cy="145" rx="160" ry="13" fill="var(--orange-dark)" opacity="0.45"/>
    <path d="M290,278 A132,14 0 0 0 554,278 L520,390 A98,11 0 0 1 324,390 Z" fill="url(#amber-band)"/>
    <path d="M324,390 A98,11 0 0 0 520,390 L484,495 Q422,520 360,495 Z" fill="url(#yellow-band)"/>

    <text class="band-head" x="340" y="214" font-size="22">PROBLEM &amp;</text>
    <text class="band-head" x="340" y="240" font-size="22">SOLUTION</text>
    <text class="band-note" x="500" y="204">SUBJECT</text>
    <text class="band-note" x="500" y="214">SHOWING</text>
    <text class="band-note" x="500" y="224">EXPERTISE</text>
    <text class="band-note" x="500" y="234">IN PROBLEM</text>

    <text class="band-head" x="346" y="326" font-size="15">PROVIDERS &amp;</text>
    <text class="band-head" x="346" y="344" font-size="15">TYPES OF</text>
    <text class="band-head" x="346" y="362" font-size="15">SOLUTION</text>
    <text class="band-note" x="466" y="326">SUBJECT</text>
    <text class="band-note" x="466" y="336">LINKED</text>
    <text class="band-note" x="466" y="346">TO THE</text>
    <text class="band-note" x="466" y="356">PROBLEM</text>

    <text class="band-head" x="422" y="440" font-size="18" text-anchor="middle">CONVERT</text>
    <text class="band-head" x="422" y="464" font-size="18" text-anchor="middle">+ RETAIN</text>
  </g>

  <!-- Referral loop -->
  <g class="referral-loop">
    <path d="M515,470 C640,440 660,200 600,110" fill="none" stroke="var(--sky-pale)" stroke-width="6" stroke-linecap="round" marker-end="url(#arrow-head)"/>
    <text class="wom" x="588" y="462">WOM &amp;</text>
    <text class="wom" x="588" y="488">REFERRAL</text>
  </g>

  <!-- Hierarchy title -->
  <g class="hierarchy-title">
    <text class="title-bold" x="190" y="688" font-size="30" fill="var(--white)">CONTENT</text>
    <text class="title-light" x="360" y="688" font-size="30" fill="var(--white)">HIERARCHY</text>
  </g>

  <!-- Pyramid -->
  <g class="pyramid">
    <g class="pyramid-front" clip-path="url(#pyramid-front)">
      <rect x="200" y="760" width="330" height="152" fill="var(--sky)"/>
      <rect x="200" y="912" width="330" height="93" fill="var(--amber)"/>
      <rect x="200" y="1005" width="330" height="65" fill="var(--orange)"/>
      <rect x="200" y="1070" width="330" height="65" fill="var(--red)"/>
    </g>
    <g class="pyramid-side">
      <polygon points="396,765 445.3,912 473.9,897.3" fill="var(--blue-light)"/>
      <polygon points="445.3,912 476.4,1005 523.1,981 473.9,897.3" fill="var(--amber-dark)"/>
      <polygon points="476.4,1005 520,1135 592,1098 523.1,981" fill="var(--red-dark)"/>
    </g>

    <text class="tier-head" x="385" y="872" text-anchor="middle" fill="var(--ink)">HERO</text>
    <text class="tier-sub" x="385" y="892" font-size="12" text-anchor="middle" fill="var(--white)">TENTPOLE CAMPAIGNS</text>
    <text class="tier-head" x="375" y="954" text-anchor="middle" fill="var(--ink)">HUB</text>
    <text class="tier-sub" x="375" y="976" font-size="12" text-anchor="middle" fill="var(--white)">REGULAR “PUSH” CONTENT</text>
    <text class="tier-head" x="365" y="1064" text-anchor="middle" fill="var(--ink)">HYGIENE</text>
    <text class="tier-sub" x="365" y="1088" font-size="12" text-anchor="middle" fill="var(--white)">ALWAYS-ON “PULL” CONTENT</text>
  </g>
</svg>
</body>
</html>
```